Design für Wohnungsexposé gesucht
Zielgruppe
nichts
Aufgabenstellung
Ich benötige ein Expose zur Vermietung einer Wohnung. Der Text ist weitestgehend fertig, Fotos existieren. Quill NLR hat einen sehr schönen Vorschlag als grafisch generiertes Design Mockup erstellt. Was ich benötige, ist auf diesen Basis den Bau eines Expose´s bei welchen ich die Texte noch selbst ändern kann.

```html
<!DOCTYPE html>
<html lang="de">
<head>
<meta charset="utf-8">
<title>Exposé – Atelier-Dachgeschoss-Wohnung</title>
<link href="https://fonts.googleapis.com/css2?family=Montserrat:wght@400;500;600;700&family=Playfair+Display:wght@400&display=swap" rel="stylesheet">
<style>
:root{
  --bg:#f1f1f0;
  --ink:#1d1c1a;
  --dark:#1f1d1b;
  --gold:#c39a4e;
  --panel:#ebebea;
  --white:#ffffff;
  --text:#2a2a2a;
}
*{margin:0;padding:0;box-sizing:border-box}
html,body{width:848px;height:1200px;overflow:hidden;background:var(--bg)}
body{position:relative;font-family:"Montserrat",sans-serif;color:var(--text)}
.abs{position:absolute}
.serif{font-family:"Playfair Display",serif;font-weight:400}
.kicker{position:absolute;color:var(--gold);font-weight:700;font-size:7px;letter-spacing:1.6px}
.kicker::after{content:"";position:absolute;left:0;top:12px;width:21px;height:1px;background:var(--gold)}
.photo{position:absolute}
.shadow{box-shadow:0 6px 10px rgba(0,0,0,.12)}

/* Cover */
.cover{left:98px;top:110px;width:326px;height:460px;background:linear-gradient(180deg,#1c1b19 0%,#25231f 45%,#3a3631 65%,#22201d 100%)}
.cover-frame{left:118px;top:125px;width:288px;height:430px;border:1px solid var(--gold)}
.cover-center{left:98px;width:326px;text-align:center}
.cover-kicker{top:172px;color:var(--gold);font-size:11px;letter-spacing:.5px}
.cover-title{top:196px;color:#fff;font-size:29px;line-height:39.5px}
.cover-rule{left:243px;top:330px;width:37px;height:1px;background:var(--gold)}
.cover-sub{top:345px;font-size:9px;letter-spacing:1.8px;line-height:14px;color:#fff}
.cover-sub .gold{color:var(--gold)}
.cover-agent{top:506px;font-size:8px;letter-spacing:1.8px;line-height:12px;color:#fff}

/* Lage */
.lage-panel{left:424px;top:110px;width:158px;height:349px;background:var(--panel)}
.map{left:582px;top:110px;width:168px;height:349px;background:linear-gradient(160deg,#e4e7df 0%,#eceee8 45%,#e1e6da 100%)}
.lage-white{left:424px;top:459px;width:326px;height:111px;background:var(--white)}
.lage-head{left:441px;top:157px;font-size:12px;color:var(--ink)}
.lage-copy{left:441px;top:185px;width:125px;font-size:5.5px;line-height:8.2px;color:var(--ink)}
.lage-copy p+p{margin-top:8px}
.lage-rule{left:441px;top:273px;width:123px;height:1px;background:#c9b58c}
.distances{left:441px;top:304px;width:123px;list-style:none;font-size:5.8px;color:var(--ink)}
.distances li{display:flex;align-items:center;height:14.7px}
.distances li::before{content:"";width:5px;height:5px;background:#e0cfa8;margin-right:6px}
.distances span{margin-left:auto}
.perks{left:446px;top:467px;width:289px;height:89px;background:var(--panel);display:flex}
.perk{flex:1;display:flex;flex-direction:column;align-items:center;padding-top:14px;font-size:5.3px;line-height:7.3px;text-align:center;color:#555}
.perk svg{width:22px;height:22px}
.perk i{display:block;width:21px;height:1px;background:var(--gold);margin:8px 0 6px}

/* Objektbeschreibung */
.obj-panel{left:98px;top:629px;width:174px;height:191px;background:var(--panel)}
.obj-right{left:272px;top:629px;width:152px;height:191px;background:var(--white)}
.obj-bottom{left:98px;top:820px;width:326px;height:270px;background:var(--white)}
.obj-head{left:115px;top:673px;font-size:12px;color:var(--ink)}
.obj-copy{left:115px;top:698px;width:137px;font-size:4.9px;line-height:6.6px;color:var(--ink);text-align:justify}
.obj-copy p+p{margin-top:6px}
.features{left:284px;top:672px;width:130px;list-style:none}
.features li{display:flex;align-items:center;height:42px;font-size:5px;line-height:6.6px;color:var(--ink)}
.features svg{width:26px;height:26px;flex:none;margin-right:10px}

/* Daten */
.data-panel{left:424px;top:629px;width:166px;height:416px;background:var(--panel)}
.gallery-col{left:590px;top:629px;width:160px;height:416px;background:var(--white)}
.data-row{position:absolute;left:441px;width:142px;display:flex;font-size:4.9px;line-height:6.5px;color:var(--ink)}
.data-row b{font-weight:400;width:50px;flex:none}
.contact{left:435px;top:916px;width:144px;height:112px;border:1px solid #d8bf8c;border-radius:4px}
.contact-title{left:443px;top:928px;color:var(--gold);font-weight:700;font-size:7.5px;letter-spacing:1.8px}
.contact-title::after{content:"";position:absolute;left:0;top:13px;width:21px;height:1px;background:var(--gold)}
.contact-line{position:absolute;left:445px;display:flex;align-items:center;font-size:7px;color:var(--ink)}
.contact-line .dot{width:10px;height:10px;border-radius:50%;background:#e2c48a;margin-right:9px;display:flex;align-items:center;justify-content:center}
.contact-agent{left:443px;top:999px;font-size:6px;letter-spacing:1px;line-height:12px;color:var(--ink)}
.band{left:424px;top:1045px;width:326px;height:45px;background:var(--dark);display:flex;align-items:center;justify-content:center;gap:12px;color:#fff;font-size:6px;letter-spacing:2.2px}
.band i{display:block;width:63px;height:1px;background:#9e9a93}
</style>
</head>
<body>

<!-- Spread 1 -->
<section class="abs shadow" style="left:98px;top:110px;width:652px;height:460px"></section>
<div class="abs cover" role="img" aria-label="Abgedunkeltes Wohnzimmerfoto mit Sofa und Parkettboden"></div>
<div class="abs cover-frame"></div>
<div class="abs cover-center cover-kicker">EXPOSÉ</div>
<h1 class="abs cover-center cover-title serif">Exclusiv.<br>Zentrumsnah.<br>Möbliert.</h1>
<div class="abs cover-rule"></div>
<div class="abs cover-center cover-sub"><span class="gold">ATELIER-DACHGESCHOSS-WOHNUNG</span><br>IN KRONBERG IM TAUNUS</div>
<div class="abs cover-center cover-agent">DIPL.-ING. LARS MUTHOVEK<br>IMMOBILIEN</div>

<div class="abs lage-panel"></div>
<div class="abs map" role="img" aria-label="Stadtplan von Kronberg im Taunus mit Lage der Wohnung und S-Bahn-Stationen"></div>
<div class="abs lage-white"></div>
<div class="kicker" style="left:441px;top:131px">LAGE</div>
<h2 class="abs lage-head serif">Eindeutig Spitzenlage!</h2>
<div class="abs lage-copy">
  <p>Die Wohnung befindet sich in ruhiger, grüner Südwest-Bestlage Kronbergs – ca. 5 Fußminuten zum Einkauf und zu zwei S-Bahn-Stationen.</p>
  <p>Das Einkaufszentrum, der Taunus sowie die Natur sind in nur 5 Minuten fußläufig erreichbar.</p>
</div>
<div class="abs lage-rule"></div>
<ul class="abs distances">
  <li>Zentrum Kronberg<span>20 min</span></li>
  <li>S-Bahn-Stationen<span>5 min</span></li>
  <li>Eschborn<span>7,5 km</span></li>
  <li>Bad Homburg<span>13 km</span></li>
  <li>Frankfurt<span>20 km</span></li>
</ul>
<div class="abs perks">
  <div class="perk">
    <svg viewBox="0 0 24 24" fill="none" stroke="#c39a4e" stroke-width="1"><path d="M2 4h3l3 11h11l2-8H7"/><circle cx="9" cy="19" r="1.5"/><circle cx="17" cy="19" r="1.5"/></svg>
    <i></i>Blick zum Taunus<br>Einkaufszentrum in<br>5 min erreichbar
  </div>
  <div class="perk">
    <svg viewBox="0 0 24 24" fill="none" stroke="#c39a4e" stroke-width="1"><path d="M12 22V9M12 15l-3-3M12 13l3-3"/><path d="M12 2c-4 0-6 3-6 6 0 3 2 5 6 5s6-2 6-5c0-3-2-6-6-6z"/></svg>
    <i></i>Natur erleben<br>In direkter Nähe zum<br>Wald und zur Natur
  </div>
  <div class="perk">
    <svg viewBox="0 0 24 24" fill="none" stroke="#c39a4e" stroke-width="1"><rect x="5" y="2" width="14" height="16" rx="2"/><path d="M5 10h14M12 2v8M8 21l2-3M16 21l-2-3"/><circle cx="8.5" cy="14" r="1"/><circle cx="15.5" cy="14" r="1"/></svg>
    <i></i>Beste Anbindung<br>Schnell in Frankfurt<br>und Umgebung
  </div>
</div>

<!-- Spread 2 -->
<section class="abs shadow" style="left:98px;top:629px;width:652px;height:461px"></section>
<div class="abs obj-panel"></div>
<div class="abs obj-right"></div>
<div class="abs obj-bottom"></div>
<div class="kicker" style="left:115px;top:651px">OBJEKTBESCHREIBUNG</div>
<h2 class="abs obj-head serif">Eindeutig erste Klasse!</h2>
<div class="abs obj-copy">
  <p>Bei dem Objekt handelt es sich um eine 2 Zimmer Dachgeschoss-Atelier-Wohnung in ruhiger, grüner Südwest-Bestlage Kronbergs.</p>
  <p>Reihenendhaus mit nur 2 Wohneinheiten, Einzelgarage und überdachter Carport. Alleinige Treppenhausnutzung mit 2 Podest-Ebenen und breitem Fensterbereich vor der Wohnungstür.</p>
  <p>Eine schließlich eine Wohnung, welche sowohl funktional als auch ästhetisch überzeugt und sich deutlich von standardisierten Wohnkonzepten abhebt.</p>
</div>
<div class="photo" style="left:98px;top:820px;width:174px;height:140px;background:linear-gradient(160deg,#f3f1ee,#e2ddd6 60%,#b9a58f)" role="img" aria-label="Helles Dachgeschoss-Wohnzimmer mit Holzbalken und Essbereich"></div>
<ul class="abs features">
  <li><svg viewBox="0 0 26 26" fill="none" stroke="#c39a4e" stroke-width="1"><rect x="4" y="3" width="12" height="20"/><path d="M8 3v20M12 3v20"/><circle cx="19" cy="20" r="3"/></svg>Durchgängige Echtholz-<br>Parkettböden</li>
  <li><svg viewBox="0 0 26 26" fill="none" stroke="#c39a4e" stroke-width="1"><rect x="2" y="5" width="22" height="16"/><path d="M13 5v16M6 17l4-8M16 17l4-8"/></svg>Ca. 6,8 m² Essbereich mit<br>Morgensonne durch große<br>Dachflächenfenster</li>
  <li><svg viewBox="0 0 26 26" fill="none" stroke="#c39a4e" stroke-width="1"><path d="M2 22l8-11 5 6 3-3 6 8z"/><circle cx="8" cy="6" r="2.5"/></svg>Blick zum Taunus<br>aus der Küche</li>
  <li><svg viewBox="0 0 26 26" fill="none" stroke="#c39a4e" stroke-width="1"><path d="M2 22h22M3 22V13h20v9M3 17h20M6 13V5h4v8"/><rect x="15" y="18" width="6" height="3"/></svg>Helle Fronten, hochwertiger<br>Elektroherd, Heltron-Backofen,<br>Geschirrspüler</li>
  <li><svg viewBox="0 0 26 26" fill="none" stroke="#c39a4e" stroke-width="1"><path d="M2 23h22M2 23v-4h5v-4h5v-4h5V7h6M4 17l18-12"/></svg>Treppen zum oberen ca. 25 m²<br>Atelierraum mit raumhohen<br>Fenstern</li>
  <li><svg viewBox="0 0 26 26" fill="none" stroke="#c39a4e" stroke-width="1"><path d="M3 23h20M4 13h18M5 13v10M9 13v10M13 13v10M17 13v10M21 13v10"/><rect x="8" y="3" width="10" height="10"/></svg>5,74 m² Südwest-<br>Dachterrasse</li>
</ul>
<div class="photo" style="left:107px;top:975px;width:96px;height:92px;background:linear-gradient(160deg,#f0eeea,#d9d4cc 70%,#a99379)" role="img" aria-label="Weiße Einbauküche"></div>
<div class="photo" style="left:213px;top:975px;width:96px;height:92px;background:linear-gradient(160deg,#6b4a33,#8a6a52 55%,#5a4538)" role="img" aria-label="Wohnbereich mit Holzdecke und Sofa"></div>
<div class="photo" style="left:320px;top:975px;width:96px;height:92px;background:linear-gradient(160deg,#eeeeec,#cfcac4 55%,#4a3638)" role="img" aria-label="Schlafzimmer mit Doppelbett"></div>

<div class="abs data-panel"></div>
<div class="abs gallery-col"></div>
<div class="kicker" style="left:441px;top:651px">DATEN &amp; KONDITIONEN</div>
<div class="data-row" style="top:682px"><b>Wohnfläche</b>ca. 55 m²</div>
<div class="data-row" style="top:705px"><b>Nutzfläche Keller</b>ca. 20 m²</div>
<div class="data-row" style="top:728px"><b>Garage</b><span>Garage mit automatischem Garagentor, überdachter Carport davor</span></div>
<div class="data-row" style="top:764px"><b>Möblierung</b><span>Komplett inkl. Spülmaschine, Herd, Backofen, Kühlschrank, eingebaute Klimaanlage, Waschmaschine und Trockner</span></div>
<div class="data-row" style="top:807px"><b>Miete</b><span>2.250 € monatlich warm<br>inkl. wöchentlicher Reinigung</span></div>
<div class="data-row" style="top:837px"><b>Kaution</b>3 Monatsmieten</div>

<div class="abs contact"></div>
<div class="abs contact-title">IHR KONTAKT</div>
<div class="contact-line" style="top:953px"><span class="dot"><svg width="6" height="6" viewBox="0 0 24 24" fill="#fff"><path d="M6 2l4 4-2 3c1 3 4 6 7 7l3-2 4 4-3 4C9 22 2 15 2 5z"/></svg></span>+49 (0) 170 48 61 903</div>
<div class="contact-line" style="top:974px"><span class="dot"><svg width="6" height="6" viewBox="0 0 24 24" fill="none" stroke="#fff" stroke-width="3"><rect x="2" y="5" width="20" height="14"/><path d="M2 5l10 8 10-8"/></svg></span>lmuthovek@raumwert.example</div>
<div class="abs contact-agent">DIPL.-ING. LARS MUTHOVEK<br>IMMOBILIEN</div>

<div class="kicker" style="left:605px;top:652px">DATEN &amp; KONDITIONEN</div>
<div class="photo" style="left:605px;top:682px;width:61px;height:109px;background:linear-gradient(180deg,#6a4a34,#d8cabb 50%,#a8683c)" role="img" aria-label="Wohnzimmer mit Galerie und Hängeleuchten"></div>
<div class="photo" style="left:675px;top:682px;width:61px;height:109px;background:linear-gradient(180deg,#efe9e1,#d9cfc2 60%,#b58a63)" role="img" aria-label="Küche mit Marmorinsel"></div>
<div class="photo" style="left:605px;top:801px;width:61px;height:109px;background:linear-gradient(180deg,#d6d4d0,#6c6660 55%,#8a847d)" role="img" aria-label="Badezimmer mit Badewanne"></div>
<div class="photo" style="left:675px;top:801px;width:61px;height:109px;background:linear-gradient(180deg,#f2f2f0,#e6e2dc 40%,#9a5a24)" role="img" aria-label="Holztreppe zum Atelier"></div>
<div class="photo" style="left:605px;top:919px;width:61px;height:109px;background:linear-gradient(180deg,#5c5a58,#8d8780 50%,#a8a39c)" role="img" aria-label="Flur mit Sessel und Pflanze"></div>
<div class="photo" style="left:675px;top:919px;width:61px;height:109px;background:linear-gradient(180deg,#f1f1ef,#e8e6e2 60%,#c6b69e)" role="img" aria-label="Heller Raum mit weißer Tür"></div>

<div class="abs band"><i></i>EXCLUSIV · ZENTRUMSNAH · MÖBLIERT<i></i></div>

</body>
</html>
```